Brightwave Travel and Tours

Hotel Reservations
Airline Ticketing
Day Tour

My business is a Travel agency. My services are issuing domestic and international tickets. Book room/hotel reservations local/international.
My color preference is apple green/orange/red/blue.
Images of beaches, tickets,luggage.

```html
<!DOCTYPE html>
<html lang="en">
<head>
<meta charset="utf-8">
<title>Brightwave Travel and Tours – Business Card</title>
<link rel="stylesheet" href="https://fonts.googleapis.com/css2?family=Nunito+Sans:wght@400;600;800&display=swap">
<style>
  :root {
    --stage: #ececec;
    --card-white: #f7f7f7;
    --panel-grey: #d9d9d9;
    --brand-blue: #2a87b5;
    --brand-teal: #1c8fb8;
    --ink: #1d1d1d;
  }
  * { box-sizing: border-box; margin: 0; padding: 0; }
  html, body { width: 1200px; height: 800px; overflow: hidden; }
  body {
    background: var(--stage);
    font-family: "Nunito Sans", Arial, sans-serif;
    position: relative;
  }
  .card {
    position: absolute;
    top: 250px;
    width: 525px;
    height: 300px;
    box-shadow: 0 6px 18px rgba(0,0,0,0.12);
    overflow: hidden;
  }

  /* Back face */
  .card--back {
    left: 50px;
    background: var(--card-white);
    padding: 8px;
  }
  .back-field {
    position: relative;
    width: 100%;
    height: 100%;
    background: var(--brand-blue);
  }
  .back-field__rule {
    position: absolute;
    left: 0; right: 0;
    top: 50%;
    height: 3px;
    transform: translateY(-50%);
    background: var(--card-white);
  }
  .back-field__seal {
    position: absolute;
    left: 50%; top: 50%;
    width: 200px; height: 200px;
    transform: translate(-50%, -50%);
    border-radius: 50%;
    background: var(--card-white);
    display: flex;
    flex-direction: column;
    align-items: center;
    justify-content: center;
    gap: 8px;
  }

  /* Brand lockup */
  .brand-dot {
    width: 40px; height: 40px;
    border-radius: 50%;
    background: var(--brand-teal);
  }
  .brand-name {
    font-weight: 800;
    color: var(--brand-teal);
    text-align: center;
    line-height: 1.1;
    font-size: 17px;
  }

  /* Front face */
  .card--front {
    left: 625px;
    background: var(--card-white);
  }
  .front-panel {
    position: absolute;
    inset: 0;
  }
  .front-brand {
    position: absolute;
    left: 0; top: 42px;
    width: 205px;
    display: flex;
    flex-direction: column;
    align-items: center;
    gap: 8px;
  }
  .services {
    position: absolute;
    left: 0; top: 190px;
    width: 205px;
    list-style: none;
    text-align: center;
    color: var(--brand-teal);
    font-size: 16px;
    line-height: 1.4;
  }
  .person {
    position: absolute;
    left: 250px; top: 58px;
    color: var(--ink);
  }
  .person__name { font-size: 22px; font-weight: 600; }
  .person__role { font-size: 15px; letter-spacing: 0.5px; }
  .contacts {
    position: absolute;
    left: 250px; top: 125px;
    list-style: none;
    color: var(--ink);
    font-size: 11px;
  }
  .contacts li {
    display: flex;
    align-items: flex-start;
    gap: 10px;
    margin-bottom: 7px;
    line-height: 1.2;
  }
  .contacts svg { flex: none; width: 18px; height: 18px; }
</style>
</head>
<body>

  <section class="card card--back" aria-label="Card back">
    <div class="back-field">
      <div class="back-field__rule"></div>
      <div class="back-field__seal">
        <span class="brand-dot"></span>
        <p class="brand-name">Brightwave<br>Travel and Tours</p>
      </div>
    </div>
  </section>

  <section class="card card--front" aria-label="Card front">
    <svg class="front-panel" width="525" height="300" viewBox="0 0 525 300">
      <path d="M225 0 H525 V300 H225 V120 L205 100 L225 80 Z" fill="var(--panel-grey)"/>
      <rect x="225" y="250" width="300" height="18" fill="var(--brand-blue)"/>
    </svg>

    <div class="front-brand">
      <span class="brand-dot"></span>
      <p class="brand-name">Brightwave<br>Travel and Tours</p>
    </div>

    <ul class="services">
      <li>Hotel Reservations</li>
      <li>Airline Ticketing</li>
      <li>Day Tour</li>
    </ul>

    <div class="person">
      <p class="person__name">Clara Benton</p>
      <p class="person__role">DIRECTOR</p>
    </div>

    <ul class="contacts">
      <li>
        <svg viewBox="0 0 18 18"><rect width="18" height="18" fill="var(--ink)"/><path d="M4 6 q5 -4 10 0 v2 h-3 v-1 h-4 v1 h-3 z M5 9 h8 v5 h-8 z" fill="#fff"/></svg>
        <span>123456789</span>
      </li>
      <li>
        <svg viewBox="0 0 18 18"><rect width="18" height="18" fill="var(--ink)"/><circle cx="9" cy="9" r="5" fill="none" stroke="#fff" stroke-width="1.5"/><path d="M4 9 H14 M9 4 V14" stroke="#fff" stroke-width="1"/></svg>
        <span>clara@brightwave.example</span>
      </li>
      <li>
        <svg viewBox="0 0 18 18"><rect width="18" height="18" fill="var(--ink)"/><path d="M9 15 L5 9 A4 4 0 1 1 13 9 Z" fill="#fff"/><circle cx="9" cy="7.5" r="1.5" fill="var(--ink)"/></svg>
        <span>Address Line 1<br>Address Line 2</span>
      </li>
    </ul>
  </section>

</body>
</html>
```